DeskHarbor - Coworking website design

DeskHarbor is a new global coworking brand, growing fast and establishing stylish locations and communities that inspire innovation and collaboration all around the world.
The project includes a complete website design, focused on delivering the company’s values and messages, provide information to site visitors and to generate leads.

Please review the attached design brief, for more information.

Target Market(s)

Both men and women. Decision makers in:
Small & medium businesses in various fields, but mainly technology firms (Startups or established brands).
Global enterprises.
Dynamic “new generation” companies.
Press

Number of Pages Required

2 page

Requirements
Must have
• Project Scope & deliverables:
• Concept and design for :
• Home page
• Deliver the values mentioned above.
• Showcase the cities in which the company has locations in.
• Show customer testimonials.
• Provide an interface (form) for booking a tour and/or leaving contact details for more information (two alternatives)
• Coworking location page - Each location is in the coolest part of a different major city, and has its own address, set of amenities (kitchen, fast internet etc,), area information (public transportation accessibility, sites near by, bars and restaurants in walking distance) and pricing for private offices (based on number of people per office). Each location page must have an interface to book a location tour.
• Site Navigation (header & footer) - allow simple navigation between multiple city pages, location pages and homepage. Growth of up to 50 locations in 25 cities.
• The navigation should account for Navigation to additional pages (not commissioned in this project) such as:
• Locations
• Enterprise
• Special promotions
• Blog
• Contact us
• About us
• Note - the site should account for geolocation variable display, showing different content for different locations.
• Deliverables must include all editable graphic files (photoshop or similar), as follows:
• Home page - Desktop view (preferably both)
• Location page - Mobile web view (preferably both)
• Navigation - both options

```html
<!DOCTYPE html>
<html lang="en">
<head>
<meta charset="utf-8">
<title>DeskHarbor – Coworking</title>
<link rel="stylesheet" href="https://fonts.googleapis.com/css2?family=Oswald:wght@400;500;600&family=Open+Sans:wght@400;600;700&display=swap">
<style>
:root{
  --blue:#0e3b82;
  --blue-deep:#0a2f6b;
  --ink:#1f2530;
  --text:#5b6068;
  --muted:#9aa0a8;
  --line:#e3e5e8;
  --field:#ececec;
  --white:#ffffff;
  --panel:#f4f4f4;
}
*{box-sizing:border-box;margin:0;padding:0}
html,body{width:1200px;height:4176px;overflow:hidden;background:var(--white)}
body{position:relative;font-family:"Open Sans",Arial,sans-serif;color:var(--text)}
.abs{position:absolute}
.head{font-family:"Oswald",Arial Narrow,sans-serif;color:var(--ink);font-weight:500;text-transform:uppercase;letter-spacing:.5px}
.btn{position:absolute;background:var(--blue);color:var(--white);font-family:"Oswald",sans-serif;font-size:13px;display:flex;align-items:center;justify-content:center;text-transform:uppercase;letter-spacing:.5px;border-radius:2px}
.ph{position:absolute}
.site-header{position:absolute;left:0;top:0;width:1200px;height:84px;background:var(--white)}
.logo{position:absolute;left:122px;top:22px;font-family:"Oswald",sans-serif;font-weight:600;font-size:32px;color:var(--blue)}
.nav{position:absolute;right:118px;top:0;height:84px;display:flex;align-items:center;gap:28px;font-family:"Open Sans",sans-serif;font-weight:700;font-size:15px;color:var(--ink)}
.nav .active{background:#eceef2;height:84px;display:flex;align-items:center;padding:0 16px}
.hero{left:0;top:84px;width:1200px;height:576px;background:linear-gradient(100deg,#6b7077 0%,#9ea3a8 35%,#c9ccd0 60%,#a7abb0 100%)}
.hero-title{position:absolute;left:0;width:1200px;top:262px;text-align:center;font-family:"Oswald",sans-serif;font-size:32px;font-weight:500;color:var(--white)}
.hero-sub{position:absolute;left:0;width:1200px;top:306px;text-align:center;font-size:14px;line-height:18px;color:var(--white);font-weight:600}
.arrow{position:absolute;top:263px;width:34px;height:34px;border-radius:50%;background:rgba(255,255,255,.85);display:flex;align-items:center;justify-content:center}
.dots{position:absolute;left:590px;top:477px;display:flex;gap:8px}
.dots i{width:9px;height:9px;border-radius:50%;background:rgba(255,255,255,.6);display:block}
.dots i.on{background:var(--white)}
.search{left:111px;top:593px;width:955px;height:137px;background:var(--panel)}
.label{position:absolute;font-size:13px;color:var(--ink)}
.field{position:absolute;background:var(--white);border:1px solid var(--line);font-size:12px;color:var(--ink);display:flex;align-items:center;padding-left:12px}
.chip{position:absolute;top:57px;height:31px;width:80px;background:var(--white);border:1px solid var(--line);font-size:12px;color:var(--ink);display:flex;align-items:center;justify-content:center}
.center{position:absolute;left:0;width:1200px;text-align:center}
.sub{font-size:14px;color:var(--text)}
.card-label{position:absolute;width:301px;text-align:center;font-family:"Oswald",sans-serif;font-size:17px;color:var(--ink);top:1168px}
.tabs{position:absolute;left:122px;top:1450px;display:flex;gap:40px;font-family:"Oswald",sans-serif;font-size:17px;color:var(--ink)}
.tabs .on{border-bottom:2px solid var(--ink);padding-bottom:4px}
.benefits{left:0;top:1771px;width:1200px;height:537px;background:linear-gradient(180deg,rgba(14,59,130,.93),rgba(10,47,107,.95)),#0e3b82}
.benefit{position:absolute;width:300px;text-align:center;color:var(--white);font-family:"Oswald",sans-serif;font-size:16px}
.benefit svg{display:block;margin:0 auto 14px}
.dotrow{position:absolute;display:flex;gap:7px}
.dotrow i{width:8px;height:8px;border-radius:50%;background:var(--blue);display:block}
.prices{left:0;top:2868px;width:1200px;height:501px;background:linear-gradient(180deg,#0f3e86,#0b3170)}
.price{position:absolute;top:2973px;width:218px;height:318px;background:var(--white);padding:8px}
.price .tier{height:40px;background:var(--blue);color:var(--white);font-family:"Oswald",sans-serif;font-size:13px;display:flex;align-items:center;justify-content:center}
.price .amount{height:56px;margin-top:6px;background:var(--blue);color:var(--white);font-family:"Oswald",sans-serif;font-size:28px;display:flex;align-items:center;justify-content:center}
.price ul{list-style:none;margin-top:6px}
.price li{height:32px;background:#f2f2f2;margin-bottom:4px;font-size:13px;color:var(--ink);display:flex;align-items:center;justify-content:center}
.price .go{height:40px;background:var(--blue);color:var(--white);font-family:"Oswald",sans-serif;font-size:18px;display:flex;align-items:center;justify-content:center;margin-top:4px}
.input{position:absolute;left:646px;width:445px;background:var(--field);font-size:13px;color:var(--ink);padding:8px 14px}
.foot-title{position:absolute;top:3888px;font-family:"Oswald",sans-serif;font-size:14px;color:var(--ink);font-weight:500}
.foot-list{position:absolute;font-size:13px;line-height:17px;color:var(--ink);list-style:none}
.bottom{left:0;top:4126px;width:1200px;height:50px;background:var(--blue)}
.social{position:absolute;top:13px;width:26px;height:26px;border-radius:50%;background:var(--white)}
</style>
</head>
<body>

<header class="site-header">
  <div class="logo">DeskHarbor</div>
  <nav class="nav">
    <span class="active">Locations</span><span>Enterprise</span><span>Special Promotions</span><span>Blog</span><span>Contact</span><span>About</span>
    <svg width="18" height="18" viewBox="0 0 18 18"><circle cx="7.5" cy="7.5" r="5.5" fill="none" stroke="#1f2530" stroke-width="2.2"/><line x1="11.5" y1="11.5" x2="16.5" y2="16.5" stroke="#1f2530" stroke-width="2.4"/></svg>
  </nav>
</header>

<section class="ph hero" role="img" aria-label="Photo of a thoughtful businessman at a laptop in a bright coworking space">
  <div class="hero-title">BRAND PERSONALITY</div>
  <div class="hero-sub">Brand personality is a set of human characteristics<br>that are attributed to a brand name.</div>
  <div class="btn" style="left:536px;top:360px;width:132px;height:34px">Read more</div>
  <div class="arrow" style="left:44px"><svg width="12" height="12" viewBox="0 0 12 12"><path d="M8 1 3 6l5 5" fill="none" stroke="#1f2530" stroke-width="2"/></svg></div>
  <div class="arrow" style="left:1122px"><svg width="12" height="12" viewBox="0 0 12 12"><path d="M4 1l5 5-5 5" fill="none" stroke="#1f2530" stroke-width="2"/></svg></div>
  <div class="dots"><i class="on"></i><i></i><i></i></div>
</section>

<section class="abs search">
  <div class="label" style="left:56px;top:30px">Where you'd like space</div>
  <div class="field" style="left:56px;top:57px;width:343px;height:31px">Choose A Location</div>
  <div class="label" style="left:437px;top:30px">How many employee</div>
  <div class="chip" style="left:437px">1-20</div>
  <div class="chip" style="left:523px">20-100</div>
  <div class="chip" style="left:609px">100-1,000</div>
  <div class="chip" style="left:695px">1,000+</div>
  <div class="btn" style="left:799px;top:58px;width:126px;height:33px">Start</div>
</section>

<section>
  <h2 class="center head" style="top:788px;font-size:30px">Enterprise</h2>
  <p class="center sub" style="top:832px">Lorem Ipsum is simply dummy typesetting industry.</p>
  <div class="ph" style="left:122px;top:877px;width:301px;height:270px;background:linear-gradient(160deg,#b8bcc2,#6e747c)" role="img" aria-label="Photo of a businessman overlooking a city skyline"></div>
  <div class="ph" style="left:451px;top:877px;width:301px;height:270px;background:linear-gradient(160deg,#c9c6c0,#7d7a75)" role="img" aria-label="Photo of a team collaborating around a table"></div>
  <div class="ph" style="left:780px;top:877px;width:301px;height:270px;background:linear-gradient(160deg,#e2e2e2,#9a9a9a)" role="img" aria-label="Photo of a minimalist designed office interior"></div>
  <div class="card-label" style="left:122px">GLOBAL ACCESS</div>
  <div class="card-label" style="left:451px">GLOBAL TEAMS</div>
  <div class="card-label" style="left:780px">SIGNATURE DESIGN</div>
  <div class="btn" style="left:535px;top:1231px;width:126px;height:31px">View more</div>
</section>

<section>
  <div class="abs head" style="left:122px;top:1378px;font-size:15px;font-weight:400">Our Services</div>
  <h2 class="abs head" style="left:122px;top:1402px;font-size:32px">Special Promotions</h2>
  <div class="tabs"><span class="on">WORKSPACE</span><span>EVENTS</span><span>NETWORK</span><span>INNOVATION</span></div>
  <p class="abs" style="left:122px;top:1508px;width:460px;font-size:13.5px;line-height:18px">Lorem Ipsum is simply dummy text of the printing and typesetting industry. Lorem Ipsum has been the industry's standard dummy text ever since the 1500s, when an unknown printer took a galley of type and scrambled it to make a type specimen book. It has survived not only five centuries</p>
  <div class="btn" style="left:122px;top:1640px;width:128px;height:31px">Read more</div>
  <div class="ph" style="left:599px;top:1358px;width:481px;height:321px;background:linear-gradient(180deg,#dfe3e6,#b5b8ba 60%,#8d8f92)" role="img" aria-label="Photo of a desk and chair by a large window with sea view"></div>
</section>

<section class="abs benefits">
  <h2 class="center head" style="top:72px;font-size:28px;color:#fff">Our Benefits</h2>
  <div class="benefit" style="left:84px;top:178px">
    <svg width="56" height="48" viewBox="0 0 56 48" fill="none" stroke="#fff" stroke-width="4" stroke-linecap="round"><path d="M6 18a32 32 0 0 1 44 0"/><path d="M14 27a20 20 0 0 1 28 0"/><path d="M22 35a9 9 0 0 1 12 0"/><circle cx="28" cy="42" r="2.5" fill="#fff"/></svg>FAST INTERNET</div>
  <div class="benefit" style="left:443px;top:174px">
    <svg width="50" height="52" viewBox="0 0 50 52" fill="none" stroke="#fff" stroke-width="3.5"><rect x="7" y="3" width="36" height="38" rx="6"/><line x1="7" y1="24" x2="43" y2="24"/><line x1="7" y1="12" x2="43" y2="12"/><circle cx="15" cy="33" r="2.5"/><circle cx="35" cy="33" r="2.5"/><line x1="13" y1="41" x2="13" y2="49"/><line x1="37" y1="41" x2="37" y2="49"/></svg>PUBLIC TRANSPORTATION</div>
  <div class="benefit" style="left:800px;top:172px">
    <svg width="58" height="54" viewBox="0 0 58 54" fill="none" stroke="#fff" stroke-width="3.5"><path d="M20 4c-3 4 3 6 0 10M30 4c-3 4 3 6 0 10"/><path d="M6 20h38v12a16 16 0 0 1-16 16h-6A16 16 0 0 1 6 32z"/><path d="M44 24h4a6 6 0 0 1 0 12h-5"/><line x1="2" y1="52" x2="50" y2="52"/></svg>KITCHEN</div>
  <div class="benefit" style="left:84px;top:342px">
    <svg width="40" height="54" viewBox="0 0 40 54" fill="none" stroke="#fff" stroke-width="3.5" stroke-linecap="round"><path d="M6 3v14a5 5 0 0 0 10 0V3M11 3v48"/><path d="M32 51V3c-6 4-8 14-8 24h8"/></svg>RESTAURANTS</div>
  <div class="benefit" style="left:443px;top:350px">
    <svg width="66" height="44" viewBox="0 0 66 44" fill="none" stroke="#fff" stroke-width="3.2"><circle cx="15" cy="12" r="7"/><circle cx="33" cy="10" r="7"/><circle cx="51" cy="12" r="7"/><path d="M3 40c0-10 6-15 12-15s12 5 12 15M21 40c0-12 6-17 12-17s12 5 12 17M39 40c0-10 6-15 12-15s12 5 12 15"/></svg>NUMBER OF PEOPLE PER</div>
  <div class="benefit" style="left:800px;top:340px">
    <svg width="54" height="56" viewBox="0 0 54 56" fill="none" stroke="#fff" stroke-width="3.2"><rect x="6" y="4" width="28" height="48"/><rect x="34" y="22" width="16" height="30"/><path d="M12 12h6M22 12h6M12 22h6M22 22h6M12 32h6M22 32h6M39 30h6M39 40h6"/><rect x="16" y="42" width="8" height="10"/></svg>OFFICES</div>
</section>

<section>
  <h2 class="abs head" style="left:122px;top:2398px;font-size:26px">Our Blog</h2>
  <p class="abs sub" style="left:122px;top:2440px">Lorem Ipsum is simply dummy text of the industry.</p>
  <div class="ph" style="left:122px;top:2492px;width:206px;height:220px;background:linear-gradient(150deg,#c8b8a4,#7a6d5e)" role="img" aria-label="Photo of people working in a coworking room"></div>
  <div class="abs" style="left:122px;top:2500px;width:38px;height:40px;background:var(--blue);color:#fff;font-size:11px;text-align:center;line-height:15px;padding-top:5px">01<br>Nov</div>
  <div class="abs head" style="left:342px;top:2498px;font-size:16px">Cloud Coworking</div>
  <div class="abs" style="left:342px;top:2524px;font-size:12px;color:var(--muted)">◷ November 03, 2017 &nbsp;&nbsp; ♡ 12</div>
  <p class="abs" style="left:342px;top:2556px;width:240px;font-size:12.5px;line-height:16px">Lorem Ipsum is simply dummy text of the printing and typesetting industry. Lorem Ipsum has been the industry's standard dummy text ever since the 1500s.</p>
  <div class="abs" style="left:342px;top:2652px;font-size:13px;color:var(--ink)">Read More ➜</div>
  <div class="dotrow" style="left:342px;top:2702px"><i></i><i></i><i></i></div>
  <div class="btn" style="left:345px;top:2759px;width:126px;height:31px">View more</div>

  <h2 class="abs head" style="left:601px;top:2398px;font-size:26px">Testimonials</h2>
  <p class="abs sub" style="left:601px;top:2440px">Lorem Ipsum is simply dummy text of the industry.</p>
  <div class="ph" style="left:601px;top:2492px;width:206px;height:220px;background:linear-gradient(150deg,#d9d6d2,#8c8884)" role="img" aria-label="Portrait photo of a smiling client"></div>
  <div class="abs head" style="left:835px;top:2498px;font-size:15px;font-weight:400">Feedback</div>
  <div class="abs head" style="left:835px;top:2524px;font-size:18px">Daniel Morrow</div>
  <div class="abs" style="left:835px;top:2552px;font-size:13px;color:var(--ink);font-weight:600">Creative Director</div>
  <div class="abs" style="left:835px;top:2568px;font-size:30px;color:var(--ink);font-family:Oswald,sans-serif">“</div>
  <p class="abs" style="left:835px;top:2608px;width:250px;font-size:12.5px;line-height:16px;text-indent:24px">Lorem Ipsum is simply dummy text of the printing and typesetting industry. Lorem Ipsum has been the industry's standard dummy</p>
  <div class="dotrow" style="left:835px;top:2702px"><i></i><i></i><i></i></div>
  <div class="btn" style="left:830px;top:2759px;width:127px;height:31px">View more</div>
</section>

<section class="abs prices">
  <h2 class="center head" style="top:48px;font-size:28px;color:#fff">Our Prices</h2>
</section>
<div class="price" style="left:122px"><div class="tier">1-10 HOURS</div><div class="amount">$100.00</div><ul><li>lorem ipsum 1</li><li>lorem ipsum 2</li><li>lorem ipsum 3</li><li>lorem ipsum 4</li></ul><div class="go">START</div></div>
<div class="price" style="left:370px"><div class="tier">10-50HOURS</div><div class="amount">$200.00</div><ul><li>lorem ipsum 1</li><li>lorem ipsum 2</li><li>lorem ipsum 3</li><li>lorem ipsum 4</li></ul><div class="go">START</div></div>
<div class="price" style="left:618px"><div class="tier">50-100-50HOURS</div><div class="amount">$400.00</div><ul><li>lorem ipsum 1</li><li>lorem ipsum 2</li><li>lorem ipsum 3</li><li>lorem ipsum 4</li></ul><div class="go">START</div></div>
<div class="price" style="left:860px"><div class="tier">200+HOURS</div><div class="amount">$800.00</div><ul><li>lorem ipsum 1</li><li>lorem ipsum 2</li><li>lorem ipsum 3</li><li>lorem ipsum 4</li></ul><div class="go">PURCHASE</div></div>

<section>
  <div class="ph" style="left:0;top:3369px;width:599px;height:451px;background:#e4e5e7" role="img" aria-label="World map showing DeskHarbor location pins"></div>
  <div class="abs head" style="left:122px;top:3410px;font-size:15px">Location Map</div>
  <svg class="abs" style="left:0;top:3369px" width="599" height="451" viewBox="0 0 599 451" fill="#0e3b82">
    <path d="M205 96c-8 0-14 6-14 14 0 10 14 24 14 24s14-14 14-24c0-8-6-14-14-14zm0 9a5 5 0 1 1 0 10 5 5 0 0 1 0-10z"/>
    <path d="M330 178c-11 0-19 8-19 19 0 14 19 32 19 32s19-18 19-32c0-11-8-19-19-19zm0 12a7 7 0 1 1 0 14 7 7 0 0 1 0-14z"/>
    <path d="M489 140c-8 0-14 6-14 14 0 10 14 24 14 24s14-14 14-24c0-8-6-14-14-14zm0 9a5 5 0 1 1 0 10 5 5 0 0 1 0-10z"/>
    <path d="M104 290c-8 0-14 6-14 14 0 10 14 24 14 24s14-14 14-24c0-8-6-14-14-14zm0 9a5 5 0 1 1 0 10 5 5 0 0 1 0-10z"/>
    <path d="M500 312c-9 0-16 7-16 16 0 12 16 28 16 28s16-16 16-28c0-9-7-16-16-16zm0 10a6 6 0 1 1 0 12 6 6 0 0 1 0-12z"/>
  </svg>
  <div class="abs head" style="left:646px;top:3410px;font-size:15px">Quick Contact</div>
  <div class="input" style="top:3466px;height:31px">Name</div>
  <div class="input" style="top:3530px;height:31px">Phone</div>
  <div class="input" style="top:3594px;height:84px">Message</div>
  <div class="btn" style="left:646px;top:3708px;width:125px;height:29px">Send</div>
</section>

<footer>
  <div class="abs" style="left:122px;top:3880px;font-family:Oswald,sans-serif;font-weight:600;font-size:28px;color:var(--blue)">DeskHarbor</div>
  <p class="abs" style="left:122px;top:3936px;width:225px;font-size:14px;line-height:18px;color:var(--ink)">Lorem Ipsum is simply dummy text of the printing and types etting industry. Lorem Ipsum has been the industry's ...</p>
  <div class="abs" style="left:122px;top:4046px;font-size:13px;color:var(--ink)">Read More ➜</div>
  <div class="foot-title" style="left:409px">QUICK LINKS</div>
  <ul class="foot-list" style="left:400px;top:3940px"><li>▸ Location</li><li>▸ Enterprise</li><li>▸ Special</li><li>▸ Promotions</li><li>▸ Blog</li><li>▸ Contact us</li><li>▸ About us</li></ul>
  <div class="foot-title" style="left:574px">ADDRESS</div>
  <ul class="foot-list" style="left:574px;top:3940px;line-height:22px"><li>48 Harbor Lane, Suite<br>210, USA</li><li style="margin-top:8px">+00 555 218 4470</li><li>info@deskharbor.com</li><li style="margin-top:8px">Mon-Sat 9:00am-6:00pm</li></ul>
  <div class="foot-title" style="left:796px">SUBSCRIBE</div>
  <div class="abs" style="left:796px;top:3944px;font-size:13px;color:var(--ink)">Get the latest updates and offer</div>
  <div class="abs" style="left:796px;top:3981px;width:229px;height:31px;border-bottom:1px solid var(--line);font-size:12px;color:var(--ink);padding:8px 10px">Enter Your Email</div>
  <div class="abs" style="left:1033px;top:3979px;width:44px;height:36px;background:var(--blue);display:flex;align-items:center;justify-content:center"><svg width="18" height="14" viewBox="0 0 18 14"><rect x="1" y="1" width="16" height="12" fill="none" stroke="#fff" stroke-width="1.6"/><path d="M1 1l8 7 8-7" fill="none" stroke="#fff" stroke-width="1.6"/></svg></div>
</footer>

<div class="abs bottom">
  <div class="abs" style="left:122px;top:15px;font-family:Oswald,sans-serif;font-size:15px;color:#fff;letter-spacing:.3px">PRIVACY POLICY - LEGAL MENTIONS - TERMS AND CONDITIONS</div>
  <span class="social" style="left:877px"></span>
  <span class="social" style="left:919px"></span>
  <span class="social" style="left:961px"></span>
  <span class="social" style="left:1003px"></span>
  <span class="social" style="left:1045px"></span>
</div>

</body>
</html>
```